Business card and stationery design

Harbour & Summit Planners is a leading event and conference design and management company.
Please view harbourandsummit.com.au

The business cards needs to convey:
- professionalism and competency
- exclusivity
- memorable experiences and quality

The business card needs to have the following aspects:
- double sided
- Full colour CMYK
- Printed on either high gloss matt card (designer to recommend)

For the business stationery we require:
- Letterhead with top banner and bottom footer
- A thank you card design
- a with compliments slip design
- a MS powerpoint and MS publisher client presentation slide design which includes cover page and then a standard presentation page
(Note- we do NOT require an envelope design- who sends letters these days!)

The company image is using the key colours of gold, silver and black.
A black background to the business card has been used before and is preferred although we are open to options.

Target Market(s)

High end corporations and businesses that require their events and conferences to be exceptionally well designed and managed

Industry/Entity Type

Business

Contact Information for Business Card

FRONT:

Darcy Whitlam
- Event and Conference Specialist

Mobile- +61 (0) 491 362 047
Office- 1300 586 917
darcyw@harbourandsummit.com.au

Web- harbourandsummit.com.au

BACK:

- Event and

Font styles to use
Other font styles liked:
• The logo designer used Trajan Pro Bold 3 for the font text in the logo

Requirements
Must have
• Amazing design of the following:
• - business card (double sided)
• - letterhead
• - client thank you card
• - powerpoint and publisher client presentation design files

```html
<!DOCTYPE html>
<html lang="en">
<head>
<meta charset="utf-8">
<title>Harbour &amp; Summit Planners – Business Card</title>
<link rel="stylesheet" href="https://fonts.googleapis.com/css2?family=Montserrat:wght@400;500;700&family=Cinzel:wght@400&display=swap">
<style>
  :root {
    --stage: #1f1f20;
    --silver: #a8a9ab;
    --charcoal: #4f4f51;
    --gold: #ddb757;
    --white: #ffffff;
    --ink-light: #f2f2f2;
  }
  html, body {
    margin: 0;
    padding: 0;
    width: 1200px;
    height: 900px;
    overflow: hidden;
    background: var(--stage);
  }
  .canvas {
    position: relative;
    width: 1200px;
    height: 900px;
  }
  .card {
    position: absolute;
    top: 285px;
    width: 540px;
    height: 330px;
    border-radius: 22px;
    overflow: hidden;
  }
  .card--back { left: 40px; background: var(--silver); }
  .card--front { left: 620px; background: var(--charcoal); }
  .card__bands {
    position: absolute;
    inset: 0;
    width: 540px;
    height: 330px;
  }

  /* back side */
  .brand-mark {
    position: absolute;
    left: 0;
    right: 0;
    top: 96px;
    text-align: center;
    font-family: "Montserrat", sans-serif;
    font-weight: 700;
    font-size: 30px;
    color: var(--gold);
    letter-spacing: 0.5px;
  }
  .back-url {
    position: absolute;
    left: 0;
    right: 0;
    top: 190px;
    text-align: center;
    font-family: "Cinzel", serif;
    font-size: 13px;
    letter-spacing: 1.5px;
    color: var(--white);
  }

  /* front side */
  .front-brand {
    position: absolute;
    left: 34px;
    top: 34px;
    width: 260px;
  }
  .front-brand__rule {
    height: 2px;
    background: var(--gold);
  }
  .front-brand__name {
    margin: 10px 0 8px;
    font-family: "Montserrat", sans-serif;
    font-weight: 700;
    font-size: 22px;
    line-height: 1.15;
    color: var(--gold);
  }
  .person {
    position: absolute;
    right: 30px;
    top: 118px;
    text-align: right;
    font-family: "Montserrat", sans-serif;
  }
  .person__name {
    font-weight: 700;
    font-size: 19px;
    color: var(--gold);
  }
  .person__role {
    margin-top: 2px;
    font-size: 11.5px;
    color: var(--ink-light);
    padding-bottom: 5px;
    border-bottom: 1.5px solid var(--ink-light);
    width: 215px;
    margin-left: auto;
  }
  .contacts {
    position: absolute;
    left: 34px;
    top: 206px;
    margin: 0;
    padding: 5px 0 0;
    list-style: none;
    border-top: 1.5px solid var(--ink-light);
    width: 330px;
    font-family: "Montserrat", sans-serif;
    font-size: 11.5px;
    color: var(--ink-light);
  }
  .contacts li {
    display: flex;
    align-items: center;
    gap: 8px;
    line-height: 17px;
  }
  .contacts svg { width: 10px; height: 10px; flex: none; }
</style>
</head>
<body>
<main class="canvas">

  <section class="card card--back" aria-label="Business card, back">
    <svg class="card__bands" viewBox="0 0 540 330" aria-hidden="true">
      <polygon points="250,262 540,262 540,272 262,272 250,282 0,282 0,276 244,276" fill="var(--white)"/>
      <polygon points="0,288 248,288 262,278 540,278 540,330 0,330" fill="var(--gold)"/>
    </svg>
    <div class="brand-mark">Harbour &amp; Summit Planners</div>
    <div class="back-url">WWW.HARBOURANDSUMMIT.COM.AU</div>
  </section>

  <section class="card card--front" aria-label="Business card, front">
    <svg class="card__bands" viewBox="0 0 540 330" aria-hidden="true">
      <polygon points="0,318 540,318 540,330 0,330" fill="var(--gold)"/>
      <polygon points="0,302 360,302 372,290 540,290 540,298 376,298 364,310 0,310" fill="var(--white)"/>
      <polygon points="372,280 386,262 540,262 540,284 372,284" fill="var(--gold)"/>
    </svg>

    <div class="front-brand">
      <div class="front-brand__rule"></div>
      <div class="front-brand__name">Harbour &amp; Summit Planners</div>
      <div class="front-brand__rule"></div>
    </div>

    <div class="person">
      <div class="person__name">Darcy Whitlam</div>
      <div class="person__role">Event and Conference Specialist</div>
    </div>

    <ul class="contacts">
      <li>
        <svg viewBox="0 0 10 10"><path d="M2 1 L4 1 L4.5 3 L3.3 3.8 Q4.2 5.8 6.2 6.7 L7 5.5 L9 6 L9 8 Q5 9 1.5 5 Q1 3 2 1Z" fill="var(--gold)"/></svg>
        1300 586 917
      </li>
      <li>
        <svg viewBox="0 0 10 10"><rect x="2.5" y="0.5" width="5" height="9" rx="1" fill="none" stroke="var(--gold)" stroke-width="1.2"/></svg>
        +61 (0) 491 362 047
      </li>
      <li>
        <svg viewBox="0 0 10 10"><rect x="0.6" y="2" width="8.8" height="6" fill="none" stroke="var(--gold)" stroke-width="1.2"/><path d="M0.6 2 L5 5.5 L9.4 2" fill="none" stroke="var(--gold)" stroke-width="1.1"/></svg>
        darcyw@harbourandsummit.com.au
      </li>
      <li>
        <svg viewBox="0 0 10 10"><circle cx="5" cy="5" r="4.3" fill="none" stroke="var(--gold)" stroke-width="1.1"/><path d="M0.7 5 H9.3 M5 0.7 Q2.5 5 5 9.3 M5 0.7 Q7.5 5 5 9.3" fill="none" stroke="var(--gold)" stroke-width="0.8"/></svg>
        www.harbourandsummit.com.au
      </li>
    </ul>
  </section>

</main>
</body>
</html>
```